DWB TAX & ACCOUNTING business card
Income tax, audit, bookkeeping, setup, training and services
Professional
Marcus Lee Varto
47 Brindell Drive
Toronto, ON K8R 4T6
dwb_tax@fernmail.ca

```html
<!DOCTYPE html>
<html lang="en">
<head>
<meta charset="utf-8">
<title>DWB Tax &amp; Accounting – Business Card</title>
<link rel="stylesheet" href="https://fonts.googleapis.com/css2?family=Arimo:wght@700&family=Questrial&display=swap">
<style>
  :root {
    --card-bg: #ffffff;
    --brand-ink: #111111;
    --ink: #111111;
    --ink-soft: #222222;
    --band-light: #e4efd8;
    --band-mid: #a9d46f;
    --band-green: #6ab023;
  }
  * { margin: 0; padding: 0; box-sizing: border-box; }
  html, body {
    width: 1200px;
    height: 687px;
    overflow: hidden;
    background: var(--card-bg);
  }
  .card {
    position: relative;
    width: 1200px;
    height: 687px;
    background: var(--card-bg);
    overflow: hidden;
  }
  .brand-name {
    position: absolute;
    left: 163px;
    top: 126px;
    color: var(--brand-ink);
    font-family: "Arimo", Arial, sans-serif;
    font-weight: 700;
    line-height: 1;
  }
  .brand-initials {
    display: block;
    font-size: 108px;
    letter-spacing: 30px;
  }
  .brand-line {
    display: block;
    margin-top: 12px;
    margin-left: 8px;
    font-size: 34.5px;
    letter-spacing: 0.3px;
  }
  .contact {
    position: absolute;
    left: 0;
    top: 0;
    color: var(--ink-soft);
    font-family: "Questrial", "Century Gothic", sans-serif;
    font-size: 31px;
    line-height: 35px;
  }
  .contact p { position: absolute; white-space: nowrap; }
  .contact-name {
    left: 727px;
    top: 154px;
    font-family: "Arimo", Arial, sans-serif;
    font-weight: 700;
    font-size: 31px;
    color: var(--ink);
  }
  .contact-address { left: 722px; top: 228px; }
  .contact-phone { left: 726px; top: 336px; }
  .contact-email { left: 726px; top: 391px; }
  .wave-band {
    position: absolute;
    left: 0;
    top: 555px;
    width: 1200px;
    height: 132px;
    background: linear-gradient(to bottom, var(--card-bg) 0%, var(--band-light) 30%, var(--band-mid) 65%, var(--band-green) 100%);
  }
</style>
</head>
<body>
  <main class="card">
    <div class="brand-name">
      <span class="brand-initials">DWB</span>
      <span class="brand-line">TAX &amp; ACCOUNTING</span>
    </div>

    <section class="contact">
      <p class="contact-name">Marcus Lee Varto</p>
      <p class="contact-address">47 Brindell Drive<br>Toronto, ON K8R 4T6</p>
      <p class="contact-phone">(416) 555-0182</p>
      <p class="contact-email">dwb_tax@fernmail.ca</p>
    </section>

    <div class="wave-band" role="img" aria-label="Decorative green and black wave along the bottom edge"></div>
  </main>
</body>
</html>
```